Financial Services Postcard Design

Lionel Budwig, CPA
Financial Services
Accounting/Tax/Consulting
Services include but not limited to
Financial Statements
Tax Returns
CFO/Controller services
Budgeting and Forecasting
Cash Management
Payroll / AP/ AR
Insurance Analysis
Cost Analysis
Special projects

I need a postcard design for my new financial service company to assist businesses in the Orange County area of southern California. I'm looking for a warm but bright look to represent CPA with many years of Management experience with manufacturing companies that can relate to business issues and provide solutions for small business.

```html
<!DOCTYPE html>
<html lang="en">
<head>
<meta charset="utf-8">
<title>Lionel Budwig, CPA – Postcard</title>
<link href="https://fonts.googleapis.com/css2?family=PT+Sans:wght@400;700&family=PT+Sans+Narrow:wght@400;700&display=swap" rel="stylesheet">
<style>
:root{
  --green:#0b7a3e;
  --green-dark:#075f2f;
  --navy:#283a8c;
  --sky:#2aa8df;
  --grey-light:#f1f1f1;
  --grey-mid:#c9c9c9;
  --ink:#2b2b2b;
  --red:#b8202a;
  --white:#ffffff;
  --stage:#e9e4dc;
}
*{margin:0;padding:0;box-sizing:border-box}
html,body{width:1200px;height:533px;overflow:hidden;background:var(--stage)}
body{position:relative;font-family:"PT Sans",Arial,sans-serif;color:var(--ink)}
.card{position:absolute;top:87px;width:474px;height:343px;overflow:hidden;box-shadow:0 2px 6px rgba(0,0,0,.25)}
.card--front{left:100px}
.card--back{left:625px;background:var(--white)}
.front-art{position:absolute;inset:0}

.brand{position:absolute;display:flex;align-items:center;gap:6px;font-weight:700;color:var(--ink);white-space:nowrap}
.brand__mark{background:var(--green);display:inline-block}
.card--front .brand{left:32px;top:24px;font-size:26px;letter-spacing:1px}
.card--front .brand__mark{width:12px;height:12px}

.address{position:absolute;color:var(--green);font-weight:700}
.card--front .address{right:20px;top:26px;font-size:11px;line-height:15px;text-align:right}

.tagline{position:absolute;left:32px;top:58px;color:var(--green);font-weight:700;font-size:16px;line-height:19px;font-variant:small-caps}

.services{position:absolute;left:36px;top:115px;color:var(--white)}
.services__title{font-weight:700;font-size:13px;font-variant:small-caps;letter-spacing:.3px;margin-bottom:8px}
.services__list{list-style:none;font-size:12.5px;line-height:15.6px;font-weight:700}
.services__list li::before{content:"• "}

.portrait{position:absolute;left:318px;top:66px;width:138px;height:205px;border:5px solid var(--green-dark);background:linear-gradient(180deg,#d8d0b6 0%,#c7b999 45%,#3a3f4c 70%,#23262e 100%)}

.slogan{position:absolute;left:180px;top:245px;width:170px;text-align:center;color:var(--white);font-weight:700;font-size:15px;line-height:20px;font-variant:small-caps;letter-spacing:.5px}

.phone-main{position:absolute;left:0;right:0;top:306px;text-align:center;font-weight:700;font-size:21px;letter-spacing:1px;color:var(--ink);display:flex;justify-content:center;align-items:center;gap:8px}
.phone-main svg{width:18px;height:18px}

/* back */
.back-panel{position:absolute;left:0;top:0;width:237px;height:343px;background:linear-gradient(90deg,#e4e4e4,#f7f7f7 70%,#ececec)}
.about{position:absolute;left:20px;top:22px;width:205px}
.about__title{color:var(--red);font-family:"PT Sans Narrow",Arial,sans-serif;font-weight:700;font-size:9.5px;margin-bottom:8px}
.about__text{font-family:"PT Sans Narrow",Arial,sans-serif;font-weight:700;font-size:8.6px;line-height:13px;color:var(--ink)}
.cta{position:absolute;left:0;width:237px;top:198px;text-align:center;color:var(--red);font-weight:700;font-size:10.5px;line-height:12px;font-family:"PT Sans Narrow",Arial,sans-serif}
.calc-photo{position:absolute;left:15px;top:205px;width:205px;height:133px;background:radial-gradient(ellipse at 30% 55%,#cfd6de 0%,#e9ecef 55%,rgba(240,240,240,0) 85%)}
.contact{position:absolute;left:62px;top:228px;font-family:"PT Sans Narrow",Arial,sans-serif;font-size:10.5px;line-height:16px;color:var(--ink)}
.contact__row{display:flex;align-items:center;gap:4px}
.contact__row svg{width:9px;height:9px}

.card--back .brand{left:252px;top:14px;font-size:14px;letter-spacing:.5px}
.card--back .brand__mark{width:8px;height:8px}
.card--back .service-line{position:absolute;left:252px;top:32px;color:var(--green);font-weight:700;font-size:8.5px;line-height:10px;font-variant:small-caps}
.card--back .address{left:278px;top:55px;font-size:8px;line-height:9.5px;color:var(--ink);font-weight:400}
.stamp{position:absolute;left:407px;top:13px;width:52px;height:47px;border:1px solid #9a9a9a}
.mail-lines{position:absolute;left:253px;top:171px;width:205px}
.mail-lines span{display:block;height:23px;border-bottom:1px solid #a8a8a8}
</style>
</head>
<body>

<section class="card card--front">
  <svg class="front-art" viewBox="0 0 474 343" preserveAspectRatio="none" aria-hidden="true">
    <defs>
      <linearGradient id="greyBg" x1="0" y1="0" x2="1" y2="1">
        <stop offset="0" stop-color="#dcdcdc"/><stop offset=".45" stop-color="#f6f6f6"/><stop offset="1" stop-color="#d2d2d2"/>
      </linearGradient>
      <linearGradient id="blueSwoosh" x1="0" y1="1" x2="1" y2="0">
        <stop offset="0" stop-color="#2b3a8f"/><stop offset=".6" stop-color="#2f6fc0"/><stop offset="1" stop-color="#2aa8df"/>
      </linearGradient>
      <linearGradient id="footBar" x1="0" y1="0" x2="0" y2="1">
        <stop offset="0" stop-color="#f4f4f4"/><stop offset="1" stop-color="#c8c8c8"/>
      </linearGradient>
    </defs>
    <rect width="474" height="343" fill="url(#greyBg)"/>
    <path d="M0 110 L330 110 Q420 106 474 96 L474 206 Q300 222 205 303 L0 303 Z" fill="#0b7a3e"/>
    <path d="M330 107 Q420 102 474 92" stroke="#ffffff" stroke-width="3" fill="none"/>
    <path d="M170 303 Q300 205 474 160 L474 303 Z" fill="url(#blueSwoosh)"/>
    <path d="M170 303 Q300 205 474 160" stroke="#ffffff" stroke-width="2.5" fill="none"/>
    <rect x="0" y="303" width="474" height="40" fill="url(#footBar)"/>
  </svg>

  <div class="brand"><span class="brand__mark"></span>Lionel Budwig, CPA</div>
  <p class="address">118 N Willowmere Ln.<br>Anaheim Hills, Ca. 92807</p>
  <p class="tagline">Financial Services<br>Accounting/Tax/Consulting</p>

  <div class="services">
    <p class="services__title">Services include but not limited to</p>
    <ul class="services__list">
      <li>Financial Statements</li>
      <li>Tax Returns</li>
      <li>CFO/Controller services</li>
      <li>Budgeting and Forecasting</li>
      <li>Cash Management</li>
      <li>Payroll / AP/ AR</li>
      <li>Insurance Analysis</li>
      <li>Cost Analysis</li>
      <li>Special projects</li>
    </ul>
  </div>

  <div class="portrait" role="img" aria-label="Portrait photo of the accountant in a dark suit and tie"></div>

  <p class="slogan">Financial Security<br>Within Reach</p>

  <p class="phone-main">
    <svg viewBox="0 0 20 20" aria-hidden="true"><circle cx="10" cy="10" r="9" fill="none" stroke="#2b2b2b" stroke-width="1.6"/><path d="M7 5 Q5 6 6 9 Q8 13 12 15 Q14 15 15 13 L13 11 L11.5 12 Q9 10.5 8 8.5 L9 7 Z" fill="#2b2b2b"/></svg>
    714.555.0142
  </p>
</section>

<section class="card card--back">
  <div class="back-panel"></div>
  <div class="about">
    <p class="about__title">ABOUT LIONEL BUDWIG, CPA</p>
    <p class="about__text">Lionel Budwig has a significant experience and an extensive record of accomplishments provide excellent qualifications as a CONTROLLER, CFO, VP of OPERATIONS and GENERAL MANAGER. A focus driven executive with passion for business whose career has been characterized by increasing responsibilities and notable achievements. Diverse responsibilities encompass operations, production, accounting and finance. Specialize in creating strategic long term plans that result in significant profitability and growth.</p>
  </div>
  <div class="calc-photo" role="img" aria-label="Photo of a calculator and pen on a financial report"></div>
  <p class="cta">CALL US NOW<br>FOR A FREE CONSULTATION</p>
  <div class="contact">
    <p class="contact__row"><svg viewBox="0 0 20 20" aria-hidden="true"><circle cx="10" cy="10" r="9" fill="none" stroke="#b8202a" stroke-width="2"/><path d="M7 5 Q5 6 6 9 Q8 13 12 15 Q14 15 15 13 L13 11 L11.5 12 Q9 10.5 8 8.5 L9 7 Z" fill="#b8202a"/></svg>714.555.0142</p>
    <p class="contact__row"><svg viewBox="0 0 20 14" aria-hidden="true"><rect x="1" y="1" width="18" height="12" fill="none" stroke="#b8202a" stroke-width="1.6"/><path d="M1 1 L10 8 L19 1" fill="none" stroke="#b8202a" stroke-width="1.6"/></svg>LionelBudwig@mailpost.net</p>
  </div>

  <div class="brand"><span class="brand__mark"></span>Lionel Budwig, CPA</div>
  <p class="service-line">Financial Services<br>Accounting/Tax/Consulting</p>
  <p class="address">118 N Willowmere Ln.<br>Anaheim Hills, Ca. 92807</p>
  <div class="stamp"></div>
  <div class="mail-lines"><span></span><span></span><span></span><span></span></div>
</section>

</body>
</html>
```